Brambleway Gardening Services. A6 flyer single sided

Need an A6 flyer designing. Single sided.
I am a gardener.
I do lawn mowing - one-off garden tidy ups or regular fortnightly visits.
All kinds of trees expertly felled, topped or pruned.
Hedge cutting.
Fencing replaced or repaired.
Fully insured.
Access to fully qualified and licenced tree arborist
07741 206319 or 01632 470918.

I have attached my business card and letter head logo.
I'm open to new designs without incorporating any of my artwork.

Industry/Entity Type

Gardener

```html
<!DOCTYPE html>
<html lang="en">
<head>
<meta charset="utf-8">
<title>Brambleway Gardening Services – A6 Flyer</title>
<link href="https://fonts.googleapis.com/css2?family=Roboto+Condensed:wght@700;800;900&family=Open+Sans:wght@600;700&display=swap" rel="stylesheet">
<style>
  :root {
    --green-deep: #0f8a3a;
    --green-mid: #35a83a;
    --green-lime: #a8cf2a;
    --green-text: #1f9a3e;
    --orange: #f26722;
    --orange-dark: #d94c12;
    --body-top: #dcdcdc;
    --body-bottom: #ffffff;
    --ink: #333333;
    --white: #ffffff;
    --frame: #8a8a8a;
  }
  * { margin: 0; padding: 0; box-sizing: border-box; }
  html, body { width: 946px; height: 1200px; overflow: hidden; background: #ffffff; }
  .flyer { position: relative; width: 946px; height: 1200px; overflow: hidden; font-family: "Open Sans", sans-serif; }
  .flyer-shapes { position: absolute; inset: 0; }

  .brand-title {
    position: absolute; left: 135px; top: 30px;
    font-family: "Roboto Condensed", sans-serif; font-weight: 800;
    font-size: 78px; line-height: 82px; color: var(--white);
    letter-spacing: 0.5px; white-space: nowrap;
    text-shadow: 0 2px 3px rgba(0,0,0,0.35);
  }
  .brand-tagline {
    position: absolute; left: 135px; top: 204px;
    font-family: "Open Sans", sans-serif; font-weight: 700;
    font-size: 35px; color: var(--white); white-space: nowrap;
    text-shadow: 0 2px 3px rgba(0,0,0,0.5);
  }

  .services-heading {
    position: absolute; left: 72px; top: 384px;
    font-weight: 600; font-size: 36px; line-height: 1.2; color: var(--green-text);
  }
  .services-list { position: absolute; left: 72px; top: 458px; width: 540px; list-style: none; }
  .services-list li {
    position: relative; padding-left: 50px; margin-bottom: 5px;
    font-weight: 600; font-size: 26px; line-height: 33px; color: var(--ink);
    white-space: nowrap;
  }
  .services-list .tick { position: absolute; left: 0; top: 4px; width: 30px; height: 26px; }

  .photo {
    position: absolute; left: 622px; width: 264px;
    border-radius: 12px; border: 3px solid var(--frame);
    box-shadow: 0 2px 5px rgba(0,0,0,0.25);
  }
  .photo-hedge { top: 441px; height: 168px; background: linear-gradient(160deg, #9aa37c 0%, #6d9a3a 45%, #4f8a23 100%); }
  .photo-border { top: 621px; height: 178px; background: linear-gradient(135deg, #2d2d2d 0%, #6d9a3a 40%, #b8d36a 100%); }
  .photo-paving { top: 810px; height: 178px; background: linear-gradient(150deg, #a6785e 0%, #8d6450 50%, #6e8f46 100%); }

  .badge-insured {
    position: absolute; left: 237px; top: 827px; width: 196px; height: 196px;
    border-radius: 50%; background: #cfcfcf; padding: 9px;
    box-shadow: 0 4px 8px rgba(0,0,0,0.4);
  }
  .badge-insured .badge-core {
    width: 100%; height: 100%; border-radius: 50%;
    border: 6px solid var(--white);
    background: radial-gradient(circle at 40% 30%, var(--orange) 0%, var(--orange-dark) 100%);
    display: flex; align-items: center; justify-content: center; text-align: center;
    font-weight: 700; font-size: 38px; line-height: 1.15; color: var(--white);
    text-shadow: 0 2px 2px rgba(0,0,0,0.35);
  }

  .contact {
    position: absolute; left: 52px; white-space: nowrap;
    font-family: "Roboto Condensed", sans-serif; font-weight: 700;
    color: var(--white); text-shadow: 0 2px 3px rgba(0,0,0,0.55);
    letter-spacing: 0.5px;
  }
  .contact-email { top: 1068px; font-size: 32px; }
  .contact-phone { top: 1118px; font-size: 37px; }
</style>
</head>
<body>
<div class="flyer">
  <svg class="flyer-shapes" viewBox="0 0 946 1200" width="946" height="1200" aria-hidden="true">
    <defs>
      <linearGradient id="headerGrad" x1="0" y1="0" x2="1" y2="0.3">
        <stop offset="0" stop-color="#0f8a3a"/>
        <stop offset="0.55" stop-color="#35a83a"/>
        <stop offset="1" stop-color="#a8cf2a"/>
      </linearGradient>
      <linearGradient id="bodyGrad" x1="0" y1="0" x2="0" y2="1">
        <stop offset="0" stop-color="#dcdcdc"/>
        <stop offset="0.45" stop-color="#ffffff"/>
      </linearGradient>
      <linearGradient id="hedgeGrad" x1="0" y1="0" x2="0" y2="1">
        <stop offset="0" stop-color="#7fb540"/>
        <stop offset="0.5" stop-color="#3f7f22"/>
        <stop offset="1" stop-color="#244e14"/>
      </linearGradient>
      <linearGradient id="grassGrad" x1="0" y1="0" x2="0.3" y2="1">
        <stop offset="0" stop-color="#5aa52b"/>
        <stop offset="1" stop-color="#2f7a1a"/>
      </linearGradient>
    </defs>

    <rect x="0" y="0" width="946" height="420" fill="url(#headerGrad)"/>
    <path role="img" aria-label="Photo of a neatly clipped green hedge" d="M0,230 C250,195 600,190 946,200 L946,420 L0,420 Z" fill="url(#hedgeGrad)"/>

    <path d="M0,228 C250,305 600,372 946,382 L946,400 C600,392 250,325 0,250 Z" fill="var(--orange)"/>
    <path d="M0,238 C250,315 600,380 946,388 L946,402 C600,396 250,332 0,262 Z" fill="var(--green-deep)"/>
    <path d="M0,250 C250,326 600,390 946,396 L946,1200 L0,1200 Z" fill="url(#bodyGrad)"/>

    <path role="img" aria-label="Photo of a freshly mown lawn" d="M0,770 C180,880 480,980 946,1010 L946,1200 L0,1200 Z" fill="url(#grassGrad)"/>
    <path d="M0,730 C120,800 230,860 330,905 L300,912 C200,872 100,815 0,758 Z" fill="var(--orange)"/>
    <path d="M0,760 C140,840 260,895 380,935 L350,940 C230,905 120,858 0,790 Z" fill="var(--green-deep)"/>
    <path d="M180,905 C420,1000 700,1030 946,1015 L946,1022 C700,1038 420,1010 180,910 Z" fill="var(--white)"/>
    <path d="M640,1015 C760,1025 860,1022 946,1012 L946,1030 C860,1036 760,1035 640,1023 Z" fill="var(--green-deep)"/>
  </svg>

  <h1 class="brand-title">BRAMBLEWAY<br>GARDENING SERVICES</h1>
  <p class="brand-tagline">&amp; Exterior Property Maintenance</p>

  <h2 class="services-heading">Our Services</h2>
  <ul class="services-list">
    <li><svg class="tick" viewBox="0 0 30 26"><path d="M2,14 L11,23 L28,3" fill="none" stroke="#1f9a3e" stroke-width="5" stroke-linecap="round" stroke-linejoin="round"/></svg>Regular fortnightly visits or one-off<br>garden tidy ups</li>
    <li><svg class="tick" viewBox="0 0 30 26"><path d="M2,14 L11,23 L28,3" fill="none" stroke="#1f9a3e" stroke-width="5" stroke-linecap="round" stroke-linejoin="round"/></svg>All kinds of trees expertly felled,<br>topped or pruned</li>
    <li><svg class="tick" viewBox="0 0 30 26"><path d="M2,14 L11,23 L28,3" fill="none" stroke="#1f9a3e" stroke-width="5" stroke-linecap="round" stroke-linejoin="round"/></svg>Hedge cutting</li>
    <li><svg class="tick" viewBox="0 0 30 26"><path d="M2,14 L11,23 L28,3" fill="none" stroke="#1f9a3e" stroke-width="5" stroke-linecap="round" stroke-linejoin="round"/></svg>Lawn mowing, Pruning, Strimming</li>
    <li><svg class="tick" viewBox="0 0 30 26"><path d="M2,14 L11,23 L28,3" fill="none" stroke="#1f9a3e" stroke-width="5" stroke-linecap="round" stroke-linejoin="round"/></svg>Fencing replaced or repaired</li>
    <li><svg class="tick" viewBox="0 0 30 26"><path d="M2,14 L11,23 L28,3" fill="none" stroke="#1f9a3e" stroke-width="5" stroke-linecap="round" stroke-linejoin="round"/></svg>Access to fully qualified and<br>licenced tree arborist</li>
  </ul>

  <div class="photo photo-hedge" role="img" aria-label="Photo of a gardener trimming a hedge with a hedge cutter"></div>
  <div class="photo photo-border" role="img" aria-label="Photo of a lawn edged with red flowers beside black railings"></div>
  <div class="photo photo-paving" role="img" aria-label="Photo of block paving being pressure washed"></div>

  <div class="badge-insured"><div class="badge-core">Fully<br>Insured</div></div>

  <p class="contact contact-email">Email: hello@bramblewaygardens.co.uk</p>
  <p class="contact contact-phone">Call @ ROB MARLOWE: 07741 206319 or 01632 470918</p>
</div>
</body>
</html>
```